Looking for a modern, Professional business card design

We have a simple business card, but are looking for a more modern, professional look. A sample of the basic card is attached as well as the logo. We would also like to add that we offer:
Struggling with your finances?
- Learn to become debt free
- Discover the power of cash
- Control your money instead of it controlling you
Let us help you achieve a new level of financial freedom!
Also, we would like to have a "SPECIAL OFFER!: FREE 30 minute consultation"
Financial Planning

```html
<!DOCTYPE html>
<html lang="en">
<head>
<meta charset="utf-8">
<title>Brightway Money Coaching – Business Card</title>
<link rel="stylesheet" href="https://fonts.googleapis.com/css2?family=Open+Sans:wght@400;700&display=swap">
<style>
  :root {
    --canvas: #e9e6e2;
    --card: #050505;
    --green: #3f9b3c;
    --lime: #8cc63f;
    --white: #ffffff;
  }
  * { box-sizing: border-box; margin: 0; padding: 0; }
  html, body { width: 1200px; height: 1000px; overflow: hidden; }
  body {
    background: var(--canvas);
    font-family: "Open Sans", Arial, sans-serif;
    color: var(--white);
    position: relative;
  }
  .card {
    position: absolute;
    left: 265px;
    width: 666px;
    height: 397px;
    background: var(--card);
    box-shadow: 0 4px 10px rgba(0,0,0,.35);
    overflow: hidden;
  }
  .card--front { top: 73px; }
  .card--back { top: 532px; }

  .front__emblem-area {
    position: absolute;
    left: 30px; top: 80px;
    width: 310px; height: 290px;
    border-radius: 50%;
    background: radial-gradient(ellipse at center, rgba(60,66,58,.55) 0%, rgba(30,32,29,.35) 45%, rgba(5,5,5,0) 72%);
  }
  .holder__name {
    position: absolute; left: 33px; top: 34px;
    font-size: 24px; font-weight: 700; color: var(--green); line-height: 1.1;
  }
  .holder__title {
    position: absolute; left: 33px; top: 62px;
    font-size: 16px; line-height: 1.2;
  }
  .contact {
    position: absolute; right: 32px; top: 36px;
    list-style: none; text-align: right;
    font-size: 16px; line-height: 25px;
  }
  .contact li { display: flex; justify-content: flex-end; align-items: center; gap: 7px; }
  .contact svg { width: 13px; height: 13px; fill: var(--green); }
  .address {
    position: absolute; right: 32px; top: 150px;
    font-size: 16px; line-height: 26px; text-align: right; font-style: normal;
  }
  .divider {
    position: absolute; left: 362px; top: 220px;
    width: 272px; height: 2px; background: var(--white);
  }
  .offer {
    position: absolute; left: 33px; top: 314px;
    font-size: 16px; line-height: 22px;
  }
  .offer__label { font-weight: 700; display: block; }

  .brand {
    position: absolute;
    display: flex; align-items: center; gap: 10px;
    font-weight: 700; color: var(--white);
  }
  .brand__dot { border-radius: 50%; background: var(--lime); flex: none; }
  .brand--front {
    left: 362px; top: 280px; width: 272px;
    font-size: 24px; line-height: 1.15;
  }
  .brand--front .brand__dot { width: 40px; height: 40px; }
  .brand--back { left: 32px; top: 82px; font-size: 25px; white-space: nowrap; }
  .brand--back .brand__dot { width: 42px; height: 42px; }

  .pitch {
    position: absolute; left: 343px; top: 198px; width: 300px;
    font-size: 16px; line-height: 21px;
  }
  .pitch__heading { font-weight: 700; margin-bottom: 11px; }
  .pitch__list { list-style: none; }
  .pitch__list li { display: flex; gap: 5px; margin-bottom: 5px; }
  .pitch__list svg { width: 14px; height: 14px; flex: none; margin-top: 4px; }
</style>
</head>
<body>

<section class="card card--front" aria-label="Business card front">
  <div class="front__emblem-area" role="img" aria-label="Faint brand emblem decoration"></div>
  <p class="holder__name">Daniel Marsh</p>
  <p class="holder__title">President</p>

  <ul class="contact">
    <li>+ 000 000 0000 <svg viewBox="0 0 16 16"><rect x="4" y="0" width="8" height="16" rx="1.5"/><rect x="5.5" y="2" width="5" height="9" fill="#050505"/></svg></li>
    <li>+ 000 000 0000 <svg viewBox="0 0 16 16"><path d="M1 5c0-2 3-3 7-3s7 1 7 3v2h-4V5H5v2H1z"/><rect x="3" y="8" width="10" height="6" rx="1"/></svg></li>
    <li>info@brightwaycoaching.com <svg viewBox="0 0 16 16"><rect x="0" y="3" width="16" height="10"/><path d="M0 3l8 6 8-6" stroke="#050505" stroke-width="1.5" fill="none"/></svg></li>
    <li>www.brightwaycoaching.com <svg viewBox="0 0 16 16"><circle cx="7" cy="7" r="6"/><path d="M8 8l7 3-3 1-1 3z" stroke="#050505" stroke-width="1"/></svg></li>
  </ul>

  <address class="address">
    48 Harbor 210 Ave, Elmford, NY 1209<br>
    PO BOX 347, Elmford, NY 1209
  </address>

  <div class="divider"></div>

  <p class="offer"><span class="offer__label">SPECIAL OFFER!:</span>FREE 30 minute consultation</p>

  <div class="brand brand--front"><span class="brand__dot"></span><span>Brightway Money Coaching</span></div>
</section>

<section class="card card--back" aria-label="Business card back">
  <div class="brand brand--back"><span class="brand__dot"></span>Brightway Money Coaching</div>

  <div class="pitch">
    <p class="pitch__heading">Struggling with your finances?</p>
    <ul class="pitch__list">
      <li><svg viewBox="0 0 16 16"><path d="M1 8l5 5L15 2" stroke="var(--lime)" stroke-width="2.5" fill="none"/></svg>Learn to become debt free</li>
      <li><svg viewBox="0 0 16 16"><path d="M1 8l5 5L15 2" stroke="var(--lime)" stroke-width="2.5" fill="none"/></svg>Discover the power of cash</li>
      <li><svg viewBox="0 0 16 16"><path d="M1 8l5 5L15 2" stroke="var(--lime)" stroke-width="2.5" fill="none"/></svg>Control your money instead of it controlling you</li>
    </ul>
    <p class="pitch__close">Let us help you achieve a new level of financial freedom!</p>
  </div>
</section>

</body>
</html>
```